Meridale Cleaning Services

In need of a business card design suited for a growing cleaning company.

We offer our cleaning and maintenance services to a wide range of clients including but not limited to the following: constuction industry, hospitality, commercial, industrial and domestic

I want the card to be very noticable, i would like people to say 'hey, great card!' when i hand them my card.double sided would be nice

we want our business to come across as exceedingly professional and innovative (different).

a contemporary design is what we have in mind
we want to present an image of a quality business with a high standard of excellence in consistent service.

i just really need a card that persuades top end quality,
our business is very certified and also strives towards environmentaly friendly alternatives
Updates

hey sorry, i have uploaded my company logo design and name
cheers.

hey guys i have added my company logo/name file on my brief page. many thanks

sorry guys a typo in the brief..
address is Tolley Rd. not Tolly Rd
thanks

Industry/Entity Type

Industrial

Requirements
Must have
• company name: meridale cleaning services
operations manager: Colm Varetti
Tel: (02)9373 6204
Fax: (02)8645 7712
Mob: 0438571490

address: 47 Tolly RD Wardley NSW 2078
Postal Adress: PO Box 5832 West Corran NSW 2116
email: meridaleclean@wexanet.com.au
website: meridalecleaningservices.com.au

```html
<!DOCTYPE html>
<html lang="en">
<head>
<meta charset="utf-8">
<title>Meridale Cleaning Services – Business Card</title>
<link rel="stylesheet" href="https://fonts.googleapis.com/css2?family=Source+Sans+3:ital,wght@0,400;0,600;0,700;1,400&display=swap">
<style>
  :root {
    --backdrop: #58585a;
    --card: #ffffff;
    --brand-blue: #1f72b8;
    --brand-green: #6aa82c;
    --ink: #3c3c3c;
    --crease: rgba(0, 0, 0, 0.22);
  }
  * { margin: 0; padding: 0; box-sizing: border-box; }
  html, body {
    width: 1200px;
    height: 962px;
    overflow: hidden;
    background: var(--backdrop);
    font-family: "Source Sans 3", Arial, sans-serif;
  }
  .stage { position: relative; width: 1200px; height: 962px; }

  .card {
    position: absolute;
    top: 110px;
    height: 740px;
    background: var(--card);
    border-radius: 28px;
  }
  .card--front { left: 196px; width: 430px; }
  .card--back  { left: 690px; width: 426px; }

  .crease {
    position: absolute;
    left: 40px;
    right: 40px;
    height: 10px;
    background: radial-gradient(ellipse at center, var(--crease) 0%, rgba(0,0,0,0.08) 45%, rgba(0,0,0,0) 72%);
  }
  .card--front .crease--top    { top: 112px; }
  .card--front .crease--bottom { top: 656px; }
  .card--back  .crease--top    { top: 114px; }
  .card--back  .crease--bottom { top: 690px; }

  /* Front: brand lockup */
  .front-mark {
    position: absolute;
    left: 120px;
    top: 240px;
    width: 190px;
    height: 190px;
  }
  .front-wordmark {
    position: absolute;
    left: 0;
    right: 0;
    top: 468px;
    text-align: center;
    color: var(--brand-blue);
    font-weight: 700;
    line-height: 1;
  }
  .front-wordmark .name { display: block; font-size: 62px; letter-spacing: -0.5px; }
  .front-wordmark .tagline { display: block; font-size: 19px; letter-spacing: 1px; margin-top: 4px; }

  /* Back: small lockup */
  .back-mark {
    position: absolute;
    left: 66px;
    top: 146px;
    width: 80px;
    height: 80px;
  }
  .back-wordmark {
    position: absolute;
    left: 158px;
    top: 152px;
    color: var(--brand-blue);
    font-weight: 700;
    line-height: 1;
  }
  .back-wordmark .name { display: block; font-size: 48px; letter-spacing: -0.5px; }
  .back-wordmark .tagline { display: block; font-size: 17px; letter-spacing: 0.6px; margin-top: 2px; }

  .contact-person {
    position: absolute;
    left: 0;
    right: 0;
    top: 286px;
    text-align: center;
    line-height: 1.2;
  }
  .contact-person .person-name { color: var(--brand-blue); font-weight: 600; font-size: 23px; }
  .contact-person .role { color: var(--brand-green); font-style: italic; font-size: 22px; }

  .phones {
    position: absolute;
    left: 0;
    right: 0;
    top: 386px;
    text-align: center;
    font-size: 22px;
    line-height: 32px;
    color: var(--ink);
  }
  .phones .label { color: var(--brand-blue); }

  .details {
    position: absolute;
    left: 20px;
    top: 532px;
    font-size: 19px;
    line-height: 29px;
    color: var(--ink);
    list-style: none;
  }
  .details .label { color: var(--brand-blue); }
</style>
</head>
<body>
<main class="stage">

  <section class="card card--front" aria-label="Card front">
    <div class="crease crease--top"></div>
    <svg class="front-mark" viewBox="0 0 192 192" aria-hidden="true">
      <circle cx="96" cy="96" r="94" fill="var(--brand-blue)"/>
    </svg>
    <h1 class="front-wordmark">
      <span class="name">Meridale</span>
      <span class="tagline">CLEANING SERVICES</span>
    </h1>
    <div class="crease crease--bottom"></div>
  </section>

  <section class="card card--back" aria-label="Card back">
    <div class="crease crease--top"></div>
    <svg class="back-mark" viewBox="0 0 80 80" aria-hidden="true">
      <circle cx="40" cy="40" r="39" fill="var(--brand-blue)"/>
    </svg>
    <h2 class="back-wordmark">
      <span class="name">Meridale</span>
      <span class="tagline">CLEANING SERVICES</span>
    </h2>

    <div class="contact-person">
      <p class="person-name">Colm Varetti</p>
      <p class="role">operations manager</p>
    </div>

    <div class="phones">
      <p><span class="label">Tel:</span> (02)9373 6204</p>
      <p><span class="label">Fax:</span> (02)8645 7712</p>
      <p><span class="label">Mob:</span> 0438571490</p>
    </div>

    <ul class="details">
      <li><span class="label">a:</span> 47 Tolly RD Wardley NSW 2078</li>
      <li><span class="label">p.a:</span> PO Box 5832 West Corran NSW 2116</li>
      <li><span class="label">e:</span> meridaleclean@wexanet.com.au</li>
      <li><span class="label">w:</span> meridalecleaningservices.com.au</li>
    </ul>
    <div class="crease crease--bottom"></div>
  </section>

</main>
</body>
</html>
```